Presentation card Venture KELO - Tech Incubator from Perú

We need a Design to promote the incubator of technology Startups.
We are in Perú, we work with a string tech filter and develop enterprenurship competencies in the Startup team.
The card is to facilitators and staff memebers of VentureKELO.
We want a clear, modern, tech and agile Design.

We work to help New enterprises of technology here in Perú, we expect the candidates have a big competencies to Research and develop technological products.

We work using methodologies from QRB, Folmestry, Brakewell and Harrowgate univeesities. Our book base is the disciplina of enterpreneur.

We work events all year using diferent formats: Brightforge, Vorne price, OPRA Model Competition you can use these logros in your Design.

Set the name, role, email, cell phone number, address.

Example:
// Contact info section
Tobías Quiroveda
Swift Modeling Hub Manager
tobias.quiroveda@kelo-example.pe
(511) 999 000 417

// Address info section
VentureKELO
Technology-based business incubator
Av. Los Cedrales 884, Valdora
Lima - Perú
web: venture-kelo-example.org.pe
email: venture@kelo-example.pe
phone number: (511) 3926508 ext. 4418

// (optional)Lema section
Making happy using technology

// Social network section
facebook: venturekelooficial

Target Market(s)

Enterprenurship, CTO, Investors, Companies interested on open innovation services

Industry/Entity Type

Information Technology

Contact Information for Business Card

Name, Role, Email, Cell phone number

Colors

Designer to choose colors to be used in the design.

Requirements
Must have
• Logo forms and colors
Nice to have
• I add pictures of the leaders of incubator
Should not have
• No vertical designs

```html
<!DOCTYPE html>
<html lang="en">
<head>
<meta charset="utf-8">
<title>Venture KELO – Business Card</title>
<link href="https://fonts.googleapis.com/css2?family=Open+Sans:wght@400;700;800&display=swap" rel="stylesheet">
<style>
  :root {
    --backdrop: #e4e4e4;
    --paper: #ffffff;
    --ink: #1b1b1b;
    --brand-pink: #d42a5a;
    --brand-pink-deep: #b81f4c;
    --swoosh-black: #1d1d1f;
    --hairline: #bdbdbd;
    --photo-top: #2f3d52;
    --photo-mid: #27324a;
    --photo-floor: #8a6a4c;
  }
  * { box-sizing: border-box; margin: 0; padding: 0; }
  html, body {
    width: 1200px; height: 864px; overflow: hidden;
    background: var(--backdrop);
    font-family: "Open Sans", Arial, sans-serif;
  }
  .canvas {
    width: 1200px; height: 864px;
    display: flex; align-items: center; justify-content: center; gap: 40px;
  }
  .card {
    position: relative;
    width: 540px; height: 309px;
    background: var(--paper);
    overflow: hidden;
    box-shadow: 0 6px 18px rgba(0,0,0,0.18);
  }
  .card-shapes { position: absolute; inset: 0; width: 100%; height: 100%; }

  /* Front */
  .holder { position: absolute; left: 36px; top: 30px; }
  .holder-name { font-size: 19px; font-weight: 700; color: var(--ink); letter-spacing: 0.2px; }
  .holder-role { font-size: 13px; color: var(--brand-pink); margin-top: 1px; }
  .contact-list { position: absolute; left: 36px; top: 128px; list-style: none; }
  .contact-item { display: flex; align-items: center; gap: 9px; font-size: 13.5px; color: var(--ink); margin-bottom: 9px; }
  .contact-icon { width: 13px; height: 13px; flex: none; }
  .brand-front {
    position: absolute; right: 40px; top: 148px;
    display: flex; align-items: center; gap: 10px;
    font-size: 32px; font-weight: 800; color: var(--ink); letter-spacing: -0.5px;
  }
  .brand-mark { width: 16px; height: 16px; background: var(--brand-pink); }

  /* Back */
  .brand-back {
    position: absolute; right: 30px; bottom: 26px;
    font-size: 26px; font-weight: 800; color: var(--paper); letter-spacing: -0.3px;
  }
</style>
</head>
<body>
<main class="canvas">

  <section class="card card-front">
    <svg class="card-shapes" viewBox="0 0 540 309" preserveAspectRatio="none" aria-hidden="true">
      <path d="M190 309 Q 360 262 540 200 L540 309 Z" fill="var(--brand-pink)"/>
      <path d="M0 176 Q 260 186 540 278 L540 292 Q 250 198 0 196 Z" fill="var(--swoosh-black)"/>
      <path d="M0 204 Q 250 208 540 300" fill="none" stroke="var(--hairline)" stroke-width="1.2"/>
    </svg>

    <div class="holder">
      <h1 class="holder-name">Tobías Quiroveda</h1>
      <p class="holder-role">Senior Software Development Engineer</p>
    </div>

    <ul class="contact-list">
      <li class="contact-item">
        <svg class="contact-icon" viewBox="0 0 14 14" aria-hidden="true">
          <rect width="14" height="14" rx="2" fill="var(--brand-pink)"/>
          <path d="M4.2 3.2 L5.8 3.2 L6.4 5.2 L5.4 6 Q6.3 7.9 8 8.6 L8.8 7.6 L10.8 8.2 L10.8 9.8 Q10.2 10.8 8.8 10.6 Q4.6 9.6 3.4 5.2 Q3.2 3.8 4.2 3.2 Z" fill="#fff"/>
        </svg>
        <span>+00 410 000 7381</span>
      </li>
      <li class="contact-item">
        <svg class="contact-icon" viewBox="0 0 14 14" aria-hidden="true">
          <rect width="14" height="14" rx="2" fill="var(--brand-pink)"/>
          <rect x="2.8" y="4" width="8.4" height="6" fill="none" stroke="#fff" stroke-width="1.1"/>
          <path d="M2.8 4 L7 7.4 L11.2 4" fill="none" stroke="#fff" stroke-width="1.1"/>
        </svg>
        <span>tobias@kelo-example.pe</span>
      </li>
    </ul>

    <div class="brand-front"><span class="brand-mark"></span>Venture KELO</div>
  </section>

  <section class="card card-back">
    <svg class="card-shapes" viewBox="0 0 540 309" preserveAspectRatio="none">
      <defs>
        <linearGradient id="team-photo-tone" x1="0" y1="0" x2="0" y2="1">
          <stop offset="0" stop-color="var(--photo-top)"/>
          <stop offset="0.6" stop-color="var(--photo-mid)"/>
          <stop offset="1" stop-color="var(--photo-floor)"/>
        </linearGradient>
      </defs>
      <rect width="540" height="309" fill="url(#team-photo-tone)" role="img" aria-label="Group photo of the incubator team in matching shirts in an office"/>
      <path d="M0 236 Q 280 262 540 150 L540 309 L0 309 Z" fill="var(--brand-pink)"/>
      <path d="M0 236 Q 280 262 540 150" fill="none" stroke="var(--brand-pink-deep)" stroke-width="2"/>
    </svg>
    <div class="brand-back">Venture KELO</div>
  </section>

</main>
</body>
</html>
```